Garnett and Lyle Personal Injury Billboard

We'd like a clean/modern billboard to build brand awareness for our law firm in the area of personal injury. Ideally, we like the word "Injured?" or something similar in large lettering.

I'm attaching images, logo and award badges which could be used. The billboards will be 14x48 ft and 10.6x36.

We are open to different color ideas, fonts, and artwork. Creative but not too busy with wording. Our web page is www.kgarnettfirm.example

Garnett & Lyle Law Firm
(555) 318-4092

```html
<!DOCTYPE html>
<html lang="en">
<head>
<meta charset="UTF-8">
<title>Garnett &amp; Lyle Law Firm — Personal Injury Billboard</title>
<link rel="stylesheet" href="https://fonts.googleapis.com/css2?family=Montserrat:wght@500;600;700&family=Oswald:wght@700&family=Barlow+Condensed:wght@400;700&display=swap">
<style>
  :root {
    --navy: #0b1d4a;
    --cream: #e6dcc6;
    --white: #ffffff;
    --grey-light: #dcdcdc;
    --grey-mid: #a9a9a9;
    --blue: #1f6fd6;
    --ink: #111418;
    --page: #eceef1;
  }
  * { box-sizing: border-box; margin: 0; padding: 0; }
  html, body { width: 1200px; height: 1200px; overflow: hidden; }
  body { background: var(--page); position: relative; }

  .billboard {
    position: absolute;
    left: 0; top: 425px;
    width: 1200px; height: 350px;
    overflow: hidden;
  }
  .library-backdrop {
    position: absolute; inset: 0;
    background: linear-gradient(90deg, #8e8e8e 0%, #bdbdbd 40%, #d9d9d9 70%, #efefef 100%);
  }
  .navy-panel { position: absolute; inset: 0; width: 1200px; height: 350px; }

  .firm-name {
    position: absolute;
    left: 92px; top: 40px;
    width: 240px;
    font-family: "Montserrat", sans-serif;
    font-weight: 600;
    color: var(--cream);
    font-size: 34px;
    line-height: 1.05;
    letter-spacing: 1px;
    text-transform: uppercase;
  }
  .firm-name .line { display: block; white-space: nowrap; }
  .firm-name .sub {
    display: block;
    font-size: 15px;
    letter-spacing: 4px;
    text-transform: none;
    margin-top: 8px;
    white-space: nowrap;
  }

  .headline {
    position: absolute;
    left: 20px; top: 140px;
    width: 350px; height: 180px;
  }
  .headline text {
    font-family: "Oswald", sans-serif;
    font-weight: 700;
    font-size: 185px;
    fill: var(--white);
  }

  .attorneys {
    position: absolute;
    left: 378px; top: 34px;
    width: 374px; height: 306px;
    background: var(--white);
    padding: 5px;
    display: flex; gap: 4px;
  }
  .attorney { position: relative; flex: 1; }
  .portrait {
    position: absolute; inset: 0 0 40px 0;
    background: linear-gradient(180deg, #5b3f33 0%, #6e6259 45%, #70727a 100%);
  }
  .attorney:first-child .portrait { inset: 0; }
  .name-tag {
    position: absolute; left: 0; bottom: 0;
    height: 40px; width: 92%;
    background: var(--white);
    clip-path: polygon(0 0, 100% 0, 88% 100%, 0 100%);
    display: flex; align-items: center;
    padding-left: 8px;
    font-family: "Barlow Condensed", sans-serif;
    font-size: 21px;
    color: var(--navy);
    text-transform: uppercase;
    white-space: nowrap;
  }
  .name-tag b { font-weight: 700; margin-left: 4px; }
  .attorney:last-child .name-tag { width: 100%; padding-left: 30px; clip-path: polygon(0 0, 100% 0, 90% 100%, 0 100%); }

  .award-badge {
    position: absolute;
    left: 886px; top: 26px;
    width: 140px; height: 196px;
    background: linear-gradient(180deg, #3fa6ea 0%, #3fa6ea 18%, #161a22 18%, #161a22 100%);
    border: 4px solid #2f9ae4;
  }

  .contact {
    position: absolute;
    left: 772px; top: 232px;
    width: 394px;
    font-family: "Montserrat", sans-serif;
  }
  .cta-bar {
    display: block;
    width: 394px;
    background: var(--blue);
    color: var(--white);
    font-size: 17px;
    font-weight: 500;
    padding: 4px 10px;
    white-space: nowrap;
    text-align: center;
  }
  .cta-bar b { font-weight: 700; }
  .phone {
    display: flex; align-items: center; gap: 10px;
    margin-top: 6px;
    font-size: 44px;
    font-weight: 700;
    color: var(--ink);
    line-height: 1;
    white-space: nowrap;
  }
  .phone svg { width: 32px; height: 32px; flex: none; }
  .web { display: block; margin-top: 4px; width: 394px; height: 36px; }
  .web text {
    font-family: "Montserrat", sans-serif;
    font-weight: 600;
    font-size: 30px;
    fill: var(--ink);
  }
</style>
</head>
<body>
  <section class="billboard" aria-label="Garnett &amp; Lyle Law Firm personal injury billboard">
    <div class="library-backdrop" role="img" aria-label="Black and white photo of a law library with bookshelves"></div>
    <svg class="navy-panel" viewBox="0 0 1200 350" preserveAspectRatio="none" aria-hidden="true">
      <polygon points="0,0 712,0 580,350 0,350" fill="var(--navy)"/>
    </svg>

    <div class="firm-name">
      <span class="line">Garnett</span>
      <span class="line">&amp; Lyle</span>
      <span class="sub">Law Firm PLLC</span>
    </div>

    <svg class="headline" viewBox="0 0 350 180" role="img" aria-label="Injured?">
      <text x="4" y="166" textLength="340" lengthAdjust="spacingAndGlyphs">INJURED?</text>
    </svg>

    <div class="attorneys">
      <div class="attorney">
        <div class="portrait" role="img" aria-label="Portrait photo of attorney Kyle M. Garnett in a grey plaid suit"></div>
        <div class="name-tag">Kyle M.<b>Garnett</b></div>
      </div>
      <div class="attorney">
        <div class="portrait" role="img" aria-label="Portrait photo of attorney Owen Lyle in a grey suit"></div>
        <div class="name-tag">Owen<b>Lyle</b></div>
      </div>
    </div>

    <div class="award-badge" role="img" aria-label="Community choice award winner badge"></div>

    <div class="contact">
      <div class="cta-bar">CONTACT FOR <b>FREE CASE EVALUATION</b></div>
      <div class="phone">
        <svg viewBox="0 0 24 24" aria-hidden="true">
          <path d="M6.6 10.8a15.1 15.1 0 0 0 6.6 6.6l2.2-2.2a1 1 0 0 1 1-.25 11.4 11.4 0 0 0 3.6.57 1 1 0 0 1 1 1V20a1 1 0 0 1-1 1A17 17 0 0 1 3 4a1 1 0 0 1 1-1h3.5a1 1 0 0 1 1 1c0 1.25.2 2.45.57 3.6a1 1 0 0 1-.25 1z" fill="var(--blue)"/>
        </svg>
        (555) 318-4092
      </div>
      <svg class="web" viewBox="0 0 394 36" role="img" aria-label="www.kgarnettfirm.example">
        <text x="2" y="28" textLength="390" lengthAdjust="spacingAndGlyphs">www.kgarnettfirm.example</text>
      </svg>
    </div>
  </section>
</body>
</html>
```